Boutique Film/TV Company needs Business Card Design

Please see our website for background on our company and look of our current logo: www.lumarocpictures.ca

Pantone 314U is our main colour.

Target Market(s)

Network of peers, funders and broadcasters.

Industry/Entity Type

Business

Requirements
Must have
• We would like rounded corners and the height of the card to be shorter than traditional (maybe?!)

It's important that we have room for our office address, office number, cell number, email address, website, facebook and linked-in info (though not all of us have a linked-in account).

Would like the logo to keep the exclamation marks over the letters but the tag line/tag words of "film - television - interactive" can stay or go or... surprise me!

Nice to have
• Silky matte finish.

We are open to a change in the font of our logo/name.

```html
<!DOCTYPE html>
<html lang="en">
<head>
<meta charset="utf-8">
<title>Lumaroc Pictures – Business Card</title>
<link rel="stylesheet" href="https://fonts.googleapis.com/css2?family=Arimo:wght@400;700&display=swap">
<style>
  :root {
    --brand-blue: #1a82ad;
    --brand-blue-deep: #156f95;
    --pattern-light: #d6e8f1;
    --pattern-mid: #8fc0d8;
    --ink-white: #ffffff;
    --backdrop: #3b3b3b;
  }
  * { margin: 0; padding: 0; box-sizing: border-box; }
  html, body { width: 1200px; height: 900px; overflow: hidden; }
  body {
    background: var(--backdrop);
    font-family: "Arimo", Arial, sans-serif;
    color: var(--ink-white);
    position: relative;
  }
  .card {
    position: absolute;
    left: 240px;
    width: 720px;
    height: 400px;
    border-radius: 22px;
    background: var(--brand-blue);
    overflow: hidden;
  }
  .card--front { top: 35px; }
  .card--back { top: 465px; }

  .pattern { position: absolute; inset: 0; width: 100%; height: 100%; }

  .wordmark {
    font-family: "Arimo", Arial, sans-serif;
    font-weight: 400;
    color: var(--ink-white);
    letter-spacing: -1px;
    line-height: 1;
  }
  .tagline {
    font-weight: 700;
    font-size: 13px;
    letter-spacing: 0.3px;
  }
  .tagline .sep { padding: 0 4px; }

  /* Front */
  .front-logo {
    position: absolute;
    left: 70px;
    top: 185px;
  }
  .front-logo .wordmark { font-size: 104px; }
  .front-logo .tagline { font-size: 17px; margin-top: 8px; padding-left: 6px; }

  /* Back */
  .back-logo { position: absolute; left: 40px; top: 34px; }
  .back-logo .wordmark { font-size: 62px; }
  .back-logo .tagline { font-size: 11px; margin-top: 5px; padding-left: 3px; }

  .contact {
    position: absolute;
    left: 40px;
    top: 160px;
    font-size: 14px;
    line-height: 1.5;
  }
  .contact .person { font-size: 18px; margin-bottom: 4px; }
  .contact .person strong { font-weight: 700; }
  .contact .social { display: flex; gap: 30px; margin-top: 4px; }
  .contact .social span { display: inline-flex; align-items: center; gap: 6px; }
  .contact .dot {
    width: 9px; height: 9px; border-radius: 50%;
    background: var(--ink-white);
    display: inline-block;
  }
</style>
</head>
<body>

  <section class="card card--front" aria-label="Business card front">
    <svg class="pattern" viewBox="0 0 720 400" role="img" aria-label="Decorative pattern of exclamation marks in light blue and white">
      <defs>
        <linearGradient id="front-band" x1="0" y1="0" x2="1" y2="1">
          <stop offset="0" stop-color="var(--pattern-light)"/>
          <stop offset="1" stop-color="var(--pattern-mid)"/>
        </linearGradient>
      </defs>
      <rect width="720" height="400" fill="var(--brand-blue-deep)" opacity="0.25"/>
      <polygon points="400,0 720,0 720,230 640,210 540,110" fill="url(#front-band)"/>
    </svg>
    <div class="front-logo">
      <div class="wordmark">Lumaroc</div>
      <div class="tagline">Films<span class="sep">•</span>Television<span class="sep">•</span>Interactive</div>
    </div>
  </section>

  <section class="card card--back" aria-label="Business card back">
    <svg class="pattern" viewBox="0 0 720 400" role="img" aria-label="Decorative pattern of light blue exclamation marks">
      <defs>
        <linearGradient id="back-band" x1="0" y1="0" x2="1" y2="1">
          <stop offset="0" stop-color="var(--pattern-mid)"/>
          <stop offset="1" stop-color="var(--pattern-light)"/>
        </linearGradient>
      </defs>
      <polygon points="720,110 720,400 420,400 470,320 560,230 640,160" fill="url(#back-band)" opacity="0.85"/>
    </svg>
    <div class="back-logo">
      <div class="wordmark">Lumaroc</div>
      <div class="tagline">Films<span class="sep">•</span>Television<span class="sep">•</span>Interactive</div>
    </div>
    <address class="contact" style="font-style: normal;">
      <div class="person"><strong>Dana Whitfield</strong> Manager</div>
      <div>42 Larchmont Avenue</div>
      <div>Toronto, ON • M4K 2P9</div>
      <div>T: 416.555.0142 • F: 416.555.0178</div>
      <div>E: info@lumarocpictures.ca • W: www.lumarocpictures.ca</div>
      <div class="social">
        <span><i class="dot"></i>/DanaWhitfield</span>
        <span><i class="dot"></i>/DanaWhitfield</span>
      </div>
    </address>
  </section>

</body>
</html>
```